Important Solar Energy Company Needs a Stationery Design

I need a modern, attractive, corporate stationary design (letter head and business card)
Attached Company Logo

Target Market(s)

Upmarket

Industry/Entity Type

Business

Colors
ec1f27
ffffff
757575
cbcbcb
000000

```html
<!DOCTYPE html>
<html lang="en">
<head>
<meta charset="utf-8">
<title>Solvanta Stationery</title>
<link rel="stylesheet" href="https://fonts.googleapis.com/css2?family=Montserrat:wght@500&family=Arimo:wght@400;700&family=Orbitron:wght@500&display=swap">
<style>
:root{
  --red:#ec1f27;
  --white:#ffffff;
  --grey:#757575;
  --light:#cbcbcb;
  --black:#000000;
  --stage:#ededed;
  --ink:#444444;
}
*{box-sizing:border-box;margin:0;padding:0}
html,body{width:1200px;height:937px;overflow:hidden}
body{background:var(--stage);position:relative;font-family:"Arimo",Arial,sans-serif;color:var(--ink)}
address{font-style:normal}
.sheet{position:absolute;background:var(--white);overflow:hidden}

/* accent area: soft red-to-black field where the decorative corner sits */
.accent{position:absolute;right:0;background:linear-gradient(180deg,var(--red) 0%,var(--black) 100%)}

.brand{position:absolute;display:flex;align-items:center;white-space:nowrap}
.brand-dot{border-radius:50%;background:var(--red);flex:none}
.brand-name{font-family:"Montserrat",Arial,sans-serif;font-weight:500;color:var(--black);letter-spacing:.12em}

/* letterhead */
.letterhead{left:185px;top:68px;width:386px;height:544px}
.letterhead .accent{bottom:0;width:34%;height:22%}
.letterhead .brand{left:18px;top:24px}
.letterhead .brand-dot{width:36px;height:36px;margin-right:9px}
.letterhead .brand-name{font-size:18px}
.lh-contact{position:absolute;left:304px;top:22px;font-size:5px;line-height:7.4px;color:#333}
.lh-contact strong{display:block;font-weight:700}
.lh-contact .icon{display:inline-block;width:4px;height:4px;background:#333;border-radius:50%;margin-right:3px;vertical-align:middle}
.letter{position:absolute;left:36px;top:138px;width:296px;font-size:5.2px;line-height:7.2px;color:#555}
.letter p{margin-bottom:7px}
.letter .gap{margin-bottom:22px}
.letter .signer{font-weight:700;color:#333}
.signature{display:block;width:30px;height:14px;background:#d9d9d9;margin:4px 0 6px}

/* cover sheet */
.cover{left:636px;top:41px;width:458px;height:576px}
.cover .accent{top:0;width:16%;height:100%}
.cover .brand{left:0;width:100%;top:220px;flex-direction:column}
.cover .brand-dot{width:84px;height:84px;margin-bottom:16px}
.cover .brand-name{font-size:33px;letter-spacing:.14em}
.site{position:absolute;font-family:"Orbitron",Arial,sans-serif;font-weight:500;color:var(--white);letter-spacing:.16em}
.cover .site{right:17px;bottom:12px;font-size:12px;color:var(--black)}
.cover .site{right:90px}

/* business cards */
.card{width:176px;height:100px;border-radius:5px;left:46px}
.card-front{top:658px}
.card-front .accent{top:0;width:16%;height:100%}
.card-front .brand{left:7px;top:8px}
.card-front .brand-dot{width:18px;height:18px;margin-right:4px}
.card-front .brand-name{font-size:9px}
.card-address{position:absolute;left:7px;top:59px;font-size:3.6px;line-height:5px;color:#333}
.card-person{position:absolute;left:90px;top:61px;font-size:4px;line-height:5px;color:#333;text-transform:uppercase}
.card-person span{display:block;text-transform:none;color:#555}
.card-lines{position:absolute;left:7px;top:78px;font-size:3.4px;line-height:5px;color:#333}
.card-back{top:785px}
.card-back .brand{left:0;width:100%;justify-content:center;top:40px}
.card-back .brand-dot{width:20px;height:20px;margin-right:5px}
.card-back .brand-name{font-size:10px}

/* envelopes */
.envelope{top:673px;width:431px;height:207px}
.envelope-front{left:265px}
.envelope-front .accent{top:0;width:18%;height:100%}
.envelope-front .brand{left:14px;top:20px}
.envelope-front .brand-dot{width:38px;height:38px;margin-right:10px}
.envelope-front .brand-name{font-size:18px}
.envelope-back{left:737px}
.flap{position:absolute;left:0;top:0;width:100%;height:70px;background:var(--black);border-radius:0 0 48px 48px}
.envelope-back .site{left:0;width:100%;text-align:center;top:27px;font-size:12.5px}
</style>
</head>
<body>

<!-- Letterhead -->
<section class="sheet letterhead">
  <div class="accent" role="img" aria-label="Red and black decorative corner"></div>
  <div class="brand"><span class="brand-dot"></span><span class="brand-name">SOLVANTA</span></div>
  <address class="lh-contact">
    <strong>Unit 4 Sunfield Park</strong>
    <strong>Harbor Road, Lisbon</strong>
    <span class="icon"></span>+351 210 555 014<br>
    <span class="icon"></span>hello@solvanta.com<br>
    <span class="icon"></span>www.solvanta.com
  </address>
  <article class="letter">
    <p>March 4, 2024</p>
    <p><span class="signer">Dear Client,</span><br>Sunfield Park, Harbor Road, Lisbon</p>
    <p>Thank you for choosing clean power for your site. Our team has reviewed your roof survey and prepared a full proposal covering panel layout, inverter sizing, storage options and expected yearly savings. Every figure is based on local sun data and current tariffs.</p>
    <p class="gap">Installation can begin within four weeks of signing, and our engineers will guide you through each step.</p>
    <p>Once the system is live, you will receive monthly reports on output and savings through your online account. Our support line stays open seven days a week, and every installation is covered by a twenty-five year performance warranty on all panels we supply.</p>
    <p>Best Regards,</p>
    <span class="signature" role="img" aria-label="Handwritten signature"></span>
    <p><span class="signer">Marta Reis</span><br>Director<br><br>Sunfield Park, Harbor Road, Lisbon</p>
  </article>
</section>

<!-- Cover sheet -->
<section class="sheet cover">
  <div class="accent" role="img" aria-label="Red and black decorative side field"></div>
  <div class="brand"><span class="brand-dot"></span><span class="brand-name">SOLVANTA</span></div>
  <span class="site">www.solvanta.com</span>
</section>

<!-- Business card, front -->
<section class="sheet card card-front">
  <div class="accent" role="img" aria-label="Red and black decorative side field"></div>
  <div class="brand"><span class="brand-dot"></span><span class="brand-name">SOLVANTA</span></div>
  <address class="card-address">Unit 4 Sunfield Park<br>Harbor Road, Lisbon</address>
  <div class="card-person">Tomas Alvim<span>Managing Director</span></div>
  <div class="card-lines">+351 210 555 014<br>hello@solvanta.com<br>www.solvanta.com</div>
</section>

<!-- Business card, back -->
<section class="sheet card card-back">
  <div class="brand"><span class="brand-dot"></span><span class="brand-name">SOLVANTA</span></div>
</section>

<!-- Envelope, front -->
<section class="sheet envelope envelope-front">
  <div class="accent" role="img" aria-label="Red and black decorative side field"></div>
  <div class="brand"><span class="brand-dot"></span><span class="brand-name">SOLVANTA</span></div>
</section>

<!-- Envelope, back -->
<section class="sheet envelope envelope-back">
  <div class="flap"></div>
  <span class="site">www.solvanta.com</span>
</section>

</body>
</html>
```